Night Dresses business cards business requirers

We are a new company initiating Mexico operations. Our core business is Night woman dress (both formal and party dress) for rent. Gownhaven is the name of the company. ITS Gownhaven form by two word. The dress word and topia (Utopic) so the place Gownhaven Means That You cant get the ideal, perfect and unique dress for your event. So we would like a modern, very creative, and attractive business card.

Industry/Entity Type

Womens Clothing

Contact Information for Business Card

Rounded Borders, two faces

Requirements
Must have
• Rounded borders, logo and slogan, modern, glam, attractive design
Should not have
• modern design classic or not

```html
<!DOCTYPE html>
<html lang="en">
<head>
<meta charset="utf-8">
<title>Gownhaven – Business Cards</title>
<link href="https://fonts.googleapis.com/css2?family=Open+Sans:wght@400;600&display=swap" rel="stylesheet">
<style>
  :root {
    --backdrop: #3b3431;
    --card: #0d0c0d;
    --card-edge: #1c1a1b;
    --orchid: #c160b4;
    --ink-light: #f2f0f1;
    --ink-muted: #d9d5d7;
  }
  * { box-sizing: border-box; margin: 0; padding: 0; }
  html, body {
    width: 1200px; height: 900px; overflow: hidden;
    background: var(--backdrop);
    font-family: "Open Sans", Arial, sans-serif;
  }
  .stage {
    position: relative; width: 1200px; height: 900px;
    display: flex; align-items: center; justify-content: center; gap: 60px;
  }
  .card {
    position: relative; width: 500px; height: 286px;
    background: var(--card);
    border: 1px solid var(--card-edge);
    border-radius: 16px;
    box-shadow: 0 14px 30px rgba(0,0,0,0.45);
    overflow: hidden;
  }
  /* Contact side */
  .card--contact { display: flex; }
  .brand-mark {
    width: 48%; display: flex; align-items: center; justify-content: center; gap: 12px;
  }
  .brand-mark__circle {
    width: 26px; height: 26px; border-radius: 50%;
    border: 3px solid var(--orchid); flex: none;
  }
  .brand-mark__name {
    color: var(--orchid); font-weight: 600; font-size: 26px;
  }
  .contact {
    width: 52%; padding: 46px 24px 0 14px; color: var(--ink-light);
  }
  .contact__name { color: var(--orchid); font-size: 20px; line-height: 1.1; }
  .contact__role { font-size: 13px; margin-top: 3px; }
  .contact__address { font-size: 13px; line-height: 1.35; margin-top: 16px; }
  .contact__list { list-style: none; margin-top: 16px; font-size: 13px; line-height: 1.55; }
  .contact__list li { display: flex; align-items: center; gap: 10px; }
  .contact__list svg { width: 11px; height: 11px; flex: none; }
  .icon-fill { fill: var(--orchid); }
  .icon-line { fill: none; stroke: var(--orchid); stroke-width: 2.4; stroke-linejoin: round; }
  /* Brand side */
  .card--brand {
    display: flex; flex-direction: column; align-items: center; justify-content: center;
  }
  .brand-circle {
    width: 68px; height: 68px; border-radius: 50%;
    border: 4px solid var(--orchid);
  }
  .wordmark {
    margin-top: 22px; color: var(--ink-light);
    font-size: 24px; font-weight: 400; letter-spacing: 7px; padding-left: 7px;
  }
  .slogan {
    margin-top: 6px; display: flex; align-items: center; gap: 8px;
    color: var(--ink-muted); font-size: 11px; letter-spacing: 4px;
  }
  .slogan::before, .slogan::after {
    content: ""; width: 28px; height: 1px; background: var(--ink-muted);
  }
</style>
</head>
<body>
<main class="stage">
  <section class="card card--contact">
    <div class="brand-mark">
      <span class="brand-mark__circle"></span>
      <span class="brand-mark__name">Gownhaven</span>
    </div>
    <div class="contact">
      <p class="contact__name">Daniela Ortega</p>
      <p class="contact__role">Managing Director</p>
      <p class="contact__address">12345, Address Goes Here<br>Country Name, 123456.</p>
      <ul class="contact__list">
        <li><svg viewBox="0 0 24 24"><path class="icon-fill" d="M6.6 10.8a15 15 0 0 0 6.6 6.6l2.2-2.2a1 1 0 0 1 1-.25 11.4 11.4 0 0 0 3.6.57 1 1 0 0 1 1 1V20a1 1 0 0 1-1 1A17 17 0 0 1 3 4a1 1 0 0 1 1-1h3.5a1 1 0 0 1 1 1c0 1.25.2 2.45.57 3.6a1 1 0 0 1-.25 1z"/></svg>055-210 478 396</li>
        <li><svg viewBox="0 0 24 24"><rect class="icon-line" x="2" y="5" width="20" height="14"/><path class="icon-line" d="M2 5l10 8 10-8"/></svg>hello@gownhaven.mx</li>
        <li><svg viewBox="0 0 24 24"><path class="icon-fill" d="M10 14a4 4 0 0 1 0-5.6l3-3a4 4 0 0 1 5.6 5.6l-1.5 1.5-1.4-1.4 1.5-1.5a2 2 0 0 0-2.8-2.8l-3 3a2 2 0 0 0 0 2.8zm4-4a4 4 0 0 1 0 5.6l-3 3a4 4 0 0 1-5.6-5.6l1.5-1.5 1.4 1.4-1.5 1.5a2 2 0 0 0 2.8 2.8l3-3a2 2 0 0 0 0-2.8z"/></svg>www.gownhaven.mx</li>
      </ul>
    </div>
  </section>

  <section class="card card--brand">
    <span class="brand-circle"></span>
    <p class="wordmark">GOWNHAVEN</p>
    <p class="slogan">GOWNS ON LOAN</p>
  </section>
</main>
</body>
</html>
```